Pinpoint Buried Network Services
Thank you all for submitting designs. You guys make it really tough to pick a design they were all good.
Thanks again.
I just added more funds to the project. I will need a word template for the letterhead.
I do not need any business card designs they are all good. Just looking at matching stationery now.
Thank you.
Please include a matching letterhead. I will add more funds to the project for stationery.
Could you include stationery.
I have attached our logo and sample biz card front and back.
Use tag line in front and list of service in back of card.
Only use contact information in the brief.

```html
<!DOCTYPE html>
<html lang="en">
<head>
<meta charset="utf-8">
<title>Pinpoint Buried Network Services — Stationery</title>
<link href="https://fonts.googleapis.com/css2?family=Oswald:wght@600&family=Open+Sans:wght@400;600&display=swap" rel="stylesheet">
<style>
:root{
  --backdrop:#3f322c;
  --paper:#ffffff;
  --ink:#1a1a1a;
  --gold:#f2b31c;
  --orange:#f49a12;
  --grey:#8a8a8a;
  --rule:#c9c9c9;
  --mist:#ececec;
}
*{box-sizing:border-box;margin:0;padding:0}
html,body{width:1200px;height:1094px;overflow:hidden;background:var(--backdrop)}
body{position:relative;font-family:"Open Sans",Arial,sans-serif;color:var(--ink)}
.sheet,.card,.envelope{position:absolute;box-shadow:0 4px 10px rgba(0,0,0,.45)}
.mark{display:flex;align-items:center;gap:5px;font-family:"Oswald",Arial,sans-serif;font-weight:600;color:var(--gold);text-transform:uppercase;line-height:1.05}
.mark i{display:block;width:12px;height:12px;background:var(--gold);flex:none}
.mark span{font-size:9px;max-width:90px}
.mark.big span{font-size:13px;max-width:130px}
.mark.big i{width:18px;height:18px}
.small{font-size:6px;line-height:1.5;color:#555}
.small b{font-weight:600;color:var(--ink)}

/* business cards */
.card{width:205px;height:108px;padding:12px;display:flex;justify-content:space-between}
.card.light{background:var(--paper)}
.card.dark{background:#111;color:#ddd}
.card.dark .small{color:#bbb}.card.dark .small b{color:var(--gold)}
.card.split{padding:0}
.card .info{align-self:center;width:92px}
.card.text-only{flex-direction:column;justify-content:center}
.half{width:50%;height:100%;padding:12px}
.half.orange{background:linear-gradient(135deg,#fbc23a,var(--orange) 60%,#c86a00)}
.half.black{background:#111}

/* letterheads */
.sheet{width:335px;background:var(--paper)}
.sheet .head{position:absolute;top:18px}
.sheet .foot{position:absolute;bottom:16px;left:22px;right:22px;display:flex;justify-content:space-between}
.watermark{position:absolute;left:40px;right:40px;background:radial-gradient(ellipse at 50% 55%,var(--mist),rgba(255,255,255,0) 70%)}
.fax-band{position:absolute;top:0;left:0;right:0;height:52px;background:#0d0d0d}
.fax-strip{position:absolute;top:0;bottom:0;left:0;width:16px;background:#0d0d0d}
.fax-title{position:absolute;top:62px;right:24px;font-family:"Oswald",Arial,sans-serif;font-size:14px}
.fax-form{position:absolute;top:86px;left:34px;right:24px;display:grid;grid-template-columns:1fr 1fr;gap:6px 14px}
.fax-form div{font-size:6px;color:#666;border-bottom:1px solid var(--rule);padding-bottom:2px}
.gold-line{position:absolute;left:0;right:0;height:3px;background:var(--gold)}

/* envelopes */
.envelope{left:74px;width:312px;background:var(--paper)}
.envelope .mark{position:absolute;left:12px;top:10px}
.flap{position:absolute;left:74px;width:312px}
</style>
</head>
<body>

<!-- business cards -->
<div class="card light" style="left:30px;top:74px">
  <div class="mark"><i></i><span>Pinpoint Buried Network Services</span></div>
  <div class="info small"><b>Tom MacPhee</b><br>Project Manager<br>P 555 210 4478<br>tmacphee@pinpointbns.com</div>
</div>
<div class="card dark" style="left:246px;top:74px">
  <div class="mark"><i></i><span>Pinpoint Buried Network Services</span></div>
  <div class="info small"><b>Tom MacPhee</b><br>Project Manager<br>P 555 210 4478<br>www.pinpointbns.com</div>
</div>
<div class="card light text-only" style="left:30px;top:187px">
  <div class="small"><b>Our Services</b><br>Utility locating and marking<br>Ground radar scanning<br>Vacuum test hole digging<br>Site mapping and reports</div>
</div>
<div class="card light text-only" style="left:246px;top:187px">
  <div class="small"><b>Finding what lies below</b><br>Safe digs start with clear marks.<br>Call before you break ground.<br>555 210 4478</div>
</div>
<div class="card split" style="left:30px;top:305px">
  <div class="half orange"><div class="mark" style="color:#111"><i style="background:#111"></i><span>Pinpoint Buried Network Services</span></div></div>
  <div class="half black small" style="color:#bbb"><b style="color:var(--gold)">Tom MacPhee</b><br>P 555 210 4478<br>tmacphee@pinpointbns.com</div>
</div>
<div class="card dark" style="left:246px;top:305px;border-left:10px solid var(--orange)">
  <div class="mark"><i></i><span>Pinpoint Buried Network Services</span></div>
  <div class="info small"><b>Utility Locating</b><br>Ground radar scans<br>Test hole digging<br>Site mapping</div>
</div>

<!-- letterhead -->
<div class="sheet" style="left:465px;top:74px;height:400px">
  <div class="head" style="left:22px"><div class="mark big"><i></i><span>Pinpoint Buried Network Services</span></div></div>
  <div class="watermark" style="top:110px;bottom:60px" role="img" aria-label="faint crew silhouette watermark"></div>
  <div class="foot small"><span>1418 Quarry Road, Suite 2<br>Harborview, PA 19010</span><span>P 555 210 4478<br>pinpointbns.com</span></div>
</div>

<!-- fax sheet -->
<div class="sheet" style="left:815px;top:74px;height:400px">
  <div class="fax-band"></div>
  <div class="fax-strip"></div>
  <div class="head" style="left:150px;top:12px"><div class="mark big"><i></i><span>Pinpoint Buried Network Services</span></div></div>
  <div class="fax-title">FAX</div>
  <div class="fax-form"><div>To:</div><div>From:</div><div>Fax:</div><div>Pages:</div><div>Phone:</div><div>Date:</div><div>Re:</div><div>CC:</div></div>
  <div class="watermark" style="top:170px;bottom:60px" role="img" aria-label="faint crew silhouette watermark"></div>
  <div class="foot small" style="left:30px"><span>1418 Quarry Road, Suite 2<br>Harborview, PA 19010</span><span>F 555 210 4479<br>pinpointbns.com</span></div>
</div>

<!-- letterhead, second page -->
<div class="sheet" style="left:465px;top:518px;height:534px">
  <div class="head" style="right:22px"><div class="mark big"><i></i><span>Pinpoint Buried Network Services</span></div></div>
  <div class="watermark" style="top:200px;bottom:70px" role="img" aria-label="faint crew silhouette watermark"></div>
  <div class="foot small"><span>1418 Quarry Road, Suite 2<br>Harborview, PA 19010</span><span style="color:var(--orange)">tmacphee@pinpointbns.com<br>555 210 4478</span></div>
</div>
<div class="sheet" style="left:815px;top:518px;height:534px">
  <div class="head" style="right:22px"><div class="mark big"><i></i><span>Pinpoint Buried Network Services</span></div></div>
  <div class="watermark" style="top:200px;bottom:70px" role="img" aria-label="faint crew silhouette watermark"></div>
  <div class="foot small"><span>1418 Quarry Road, Suite 2, Harborview, PA 19010<br>P 555 210 4478 · pinpointbns.com</span></div>
</div>

<!-- envelopes -->
<div class="envelope" style="top:474px;height:134px">
  <div class="mark"><i></i><span>Pinpoint Buried Network Services</span></div>
  <div class="small" style="position:absolute;left:12px;top:44px">1418 Quarry Road<br>Harborview, PA 19010</div>
</div>
<svg class="flap" style="top:604px" width="312" height="90" viewBox="0 0 312 90">
  <rect width="312" height="90" fill="#fafafa"/>
  <polygon points="0,0 312,0 156,70" fill="#e4e4e4" stroke="#bcbcbc"/>
</svg>
<div class="mark" style="position:absolute;left:190px;top:630px"><i></i></div>
<svg class="flap" style="top:680px" width="312" height="100" viewBox="0 0 312 100">
  <rect width="312" height="100" fill="#fafafa"/>
  <defs><linearGradient id="flapGold" x1="0" y1="0" x2="0" y2="1"><stop offset="0" stop-color="#fbc23a"/><stop offset="1" stop-color="#e88a00"/></linearGradient></defs>
  <polygon points="0,0 312,0 156,80" fill="url(#flapGold)"/>
</svg>
<div class="mark" style="position:absolute;left:222px;top:716px;color:#111"><i style="background:#111"></i></div>
<svg class="flap" style="top:768px" width="312" height="100" viewBox="0 0 312 100">
  <rect width="312" height="100" fill="#fafafa"/>
  <polygon points="0,0 312,0 156,80" fill="#111"/>
</svg>
<div class="mark" style="position:absolute;left:222px;top:800px"><i></i></div>
<div class="envelope" style="top:860px;height:134px">
  <div class="mark"><i></i><span>Pinpoint Buried Network Services</span></div>
  <div class="small" style="position:absolute;left:12px;top:44px">1418 Quarry Road<br>Harborview, PA 19010</div>
</div>

</body>
</html>
```